Comparison Website Design for Glue Website

Note: We don't have a logo, it's not needed. Just put placeholder.

We would like a website comparing A to B, simple elegant design, simplistic styling. Website is for helping people find the best glue to glue 2 things together. For example, Metal to wood, Metal to rubber, glass to fabric and so on. Select 2 options and be shown the best glue/adhesive for the job.

Purpose of the website:
Allowing someone to pick 2 materials they want to glue together, and showing them the best product for it. We want someone to select 2 materials like "Metal and Rubber". It'll then show the best glues/adhesives from best #1 to #5-10 other ones. The design is simple and doesn't need much detail.

Design rules:
Please design using bootstrap 4 with a modified 1440px width.

We're looking for 4 main pages:
Home Page, Compare Page, Category Page, Product Page.

Target Market(s)

Everyone

Industry/Entity Type

Adhesive

Number of Pages Required

3 page

Font styles to use
Sans Serif

Colors
876aae
b7a5cd
6b449b
e4daeb
fefeff

Requirements
Must have
• We like the following features of these designs:
https://pixlorum.net/works/7310284-Cavrano-Dashboard - Main menu with the drop down, this will change depending on the active page. If they are on a metal page they could be shown "glue metal to ___" options. We also like the simple table view in this design under "users" heading.

https://pixlorum.net/works/7228451-Quotation-Page - The entire colour palette is great! The simplicity of the design is great.

https://pixlorum.net/works/9107642-Comparison-UI - The boxes at the top look great, if there was 2 of these with a compare icon between them and above that saying "glue metal to rubber" and it shows an icon/image or metal and glue... The table of products is also good, it has dot points and details which we like.

https://pixlorum.net/works/5093718-Send-Funds/attachments/5093718-Send-Funds?mode=media - The right it shows which 2 products are selected (metal and rubber) for example, on the left it would say "best glue for metal and rubber". This is too detailed though, so it would need to be simplified nicely.

https://linquora.net/ - They do a good job of "comparing" 2 things and displaying integrations well. You can get lots of ideas from them linking A to B similar to what we want to show.

https://www.flowtoolreviewdesk.net/brivelo-vs-tandrix/ - This shows a good example of the hero section how it should look.

Features of each page to help you design:
Home Page-
Menu (shown in examples above)
Hero section (colour section) with a centre heading saying "what do you want to glue together" with 2 boxes below to select materials from.
List of most popular searches (metal to rubber, glass to wood, fabric to leather... repeat these to fill space).
List of popular products with basic details about each one (grid format, not list).
FAQs - You choose design for this
Content section (simple design, headings, paragraphs, dotpoints, images...)
Blog section - Simple 3 column grid with an image on top, heading, paragraph, button.

Compare Page-
Showing 2 materials in the colour hero section under or to the right of the heading and paragraph.
Best product (highlighted)
9 other products (list table)
3 column section saying glue (product a to ___) with other product that isn't product b + reverse of this.
Content section

Category page-
heading and breadcrumbs in hero section
Standard product list 1 column on the left with filters, 3 products shown on the right in grid format with basic details on each one.

Product page-
Image left, details on the right.
Keep the image smaller not 50% as we want it to not take up too much space vertically.
Under this put a table where this product ranks for gluing things together. for example #3 for gluing metal to rubber, #1 for glass to wood.
Content section.

Please note, keep this design flat, simple and pretty. We don't need it over-designed or detailed, we simply want a simple functionality website that clearly shows what we're looking for.

```html
<!DOCTYPE html>
<html lang="en">
<head>
<meta charset="utf-8">
<title>Glue Comparison – Website Pages</title>
<link href="https://fonts.googleapis.com/css2?family=Poppins:wght@300;400;500;600;700&display=swap" rel="stylesheet">
<style>
:root{
  --purple:#876aae;
  --lilac:#b7a5cd;
  --deep:#6b449b;
  --mist:#e4daeb;
  --white:#fefeff;
  --footer:#7b57aa;
  --stage:#b8a6cf;
  --ink:#2d2a33;
  --grey:#8b8794;
  --line:#e9e5ee;
  --star:#f5b51b;
}
*{box-sizing:border-box;margin:0;padding:0}
html,body{width:1200px;height:2410px;overflow:hidden}
body{background:var(--stage);font-family:'Poppins',sans-serif;color:var(--ink);position:relative}
ul{list-style:none}
.page{position:absolute;width:430px;background:var(--white);overflow:hidden;box-shadow:0 6px 24px rgba(70,40,110,.18)}
.abs{position:absolute}

/* navigation */
.nav{position:absolute;left:0;top:0;width:430px;height:32px;background:var(--white)}
.nav-logo{position:absolute;left:32px;top:9px;font-size:10px;font-weight:700;color:var(--ink)}
.nav-menu{position:absolute;left:203px;top:14px;display:flex;gap:10px;font-size:4.2px;font-weight:500;color:#444}
.nav-user{position:absolute;left:336px;top:9px;display:flex;align-items:center;gap:4px;font-size:4.3px;font-weight:600}
.avatar{width:14px;height:14px;border-radius:2px;background:linear-gradient(135deg,#5a6b86,#2e3446)}

/* hero */
.hero{position:absolute;left:0;top:32px;width:430px;background:linear-gradient(120deg,#6b449b 0%,#7449a6 60%,#6a3f9a 100%);overflow:hidden}
.hero-big{height:140px}
.hero-slim{height:50px}
.hero-title{position:absolute;left:0;width:430px;top:30px;text-align:center;color:#fff;font-size:15px;font-weight:600;line-height:19px}
.hero-slim .hero-title{top:11px;font-size:10.5px;font-weight:500;line-height:14px}
.crumbs{position:absolute;left:0;width:430px;top:27px;text-align:center;color:#fff;font-size:4.3px}
.deco-ring{position:absolute;border:1px solid rgba(255,255,255,.35);border-radius:50%}
.deco-diamond{position:absolute;width:11px;height:11px;border:1px solid rgba(255,255,255,.3);transform:rotate(45deg)}
.deco-blob{position:absolute;border-radius:50%;background:rgba(255,255,255,.05)}
.deco-plus{position:absolute;color:rgba(255,255,255,.45);font-size:14px;font-weight:300;line-height:1}

/* material pickers */
.picker{position:absolute;top:126px;width:88px;height:89px;background:var(--lilac);border-radius:6px;border-bottom:2px solid #9c86bd;text-align:center;color:#fff}
.picker svg{position:absolute;left:27px;top:14px}
.picker-label{position:absolute;left:0;width:100%;top:62px;font-size:10px;font-weight:300}
.vs{position:absolute;left:206px;top:160px;width:22px;height:22px;border-radius:50%;background:#fff;border:2px solid #d9cfe6;font-size:7.5px;font-weight:700;display:flex;align-items:center;justify-content:center}

.section-title{position:absolute;left:0;width:430px;text-align:center;font-size:10.5px;font-weight:500}

/* quick finder */
.finder-label{position:absolute;font-size:4.3px;display:flex;align-items:center;gap:3px}
.bottle-mini{width:4px;height:7px;background:var(--ink);border-radius:1px}
.stepper{position:absolute;height:9px;display:flex;align-items:center;justify-content:space-between;padding:0 4px;font-size:4.2px;border-radius:5px;background:#f3f1f6}
.track{position:absolute;height:1.5px;background:#ddd8e4}
.knob{position:absolute;width:6px;height:6px;border-radius:50%;background:#fff;border:1px solid #999;top:-2.3px}
.btn{position:absolute;background:var(--deep);color:#fff;font-size:3.9px;font-weight:600;border-radius:2px;display:flex;align-items:center;justify-content:center;letter-spacing:.2px}
.rule{position:absolute;height:1px;background:var(--line)}

/* popular searches */
.search-head{position:absolute;left:64px;top:393px;width:130px;font-size:10px;font-weight:500;line-height:11px}
.round-arrow{position:absolute;width:20px;height:20px;border-radius:50%;border:1px solid #e2dee7;font-size:7px;display:flex;align-items:center;justify-content:center;color:#777}
.tile{position:absolute;top:388px;width:58px;height:63px;background:var(--lilac);border-radius:4px;text-align:center;color:#fff;border-bottom:2px solid #a18cc0}
.tile svg{position:absolute;left:17px;top:10px}
.tile span{position:absolute;left:0;width:100%;top:49px;font-size:4.2px}

/* offer rows */
.band{position:absolute;left:0;width:430px;background:var(--mist)}
.offer{position:absolute;left:59px;width:312px;height:41px;background:#fff;border-radius:2px;box-shadow:0 1px 4px rgba(90,60,130,.08)}
.offer.top-pick{outline:1.5px solid var(--purple)}
.brand{position:absolute;left:12px;top:15px;display:flex;align-items:center;gap:3px}
.brand-dot{width:9px;height:9px;border-radius:50%;border:2px solid var(--star)}
.brand-name{font-size:5.3px;font-weight:700;color:var(--purple)}
.offer-divider{position:absolute;left:78px;top:8px;width:1px;height:25px;background:var(--line)}
.perks{position:absolute;left:84px;top:6px;font-size:3.8px;line-height:9.5px;color:var(--grey)}
.perks li::before{content:"✓ ";color:#aaa}
.rating{position:absolute;left:196px;top:12px;font-size:3.8px;color:var(--grey);line-height:6px}
.stars{display:block;color:var(--star);font-size:5.5px;letter-spacing:.3px}
.medal{position:absolute;left:176px;top:12px;width:8px;height:8px;border-radius:50%;background:#f0a42a}
.apply{position:absolute;left:250px;top:8px;width:52px;height:12px;background:var(--deep);color:#fff;font-size:3.8px;font-weight:600;border-radius:2px;display:flex;align-items:center;justify-content:center}
.users{position:absolute;left:250px;top:25px;width:52px;text-align:center;font-size:3.8px;color:#555}

/* faq */
.faq-head{position:absolute;left:31px;top:741px;font-size:11px;font-weight:500}
.faq-item{position:absolute;left:31px;width:181px;height:21px;border-bottom:1px solid var(--line);font-size:4.3px;display:flex;align-items:center;gap:6px;padding-left:6px}
.faq-item b{font-weight:300;font-size:7px;color:#777}
.faq-answer{position:absolute;left:47px;top:862px;width:160px;font-size:4px;line-height:7.4px;color:var(--grey)}
.ph{position:absolute}

/* biography */
.bio-kicker{position:absolute;left:238px;top:950px;font-size:12px;font-weight:500;color:var(--lilac)}
.bio-title{position:absolute;left:238px;top:961px;font-size:22px;font-weight:600}
.bio-line{position:absolute;left:238px;top:1002px;width:26px;height:1px;background:var(--ink)}
.bio-text{position:absolute;left:272px;top:998px;width:130px;font-size:4.1px;line-height:7.4px;color:var(--grey)}
.bio-list{position:absolute;left:264px;top:1031px;font-size:4.1px;line-height:9.6px;color:#555}
.bio-list li::before{content:"";display:inline-block;width:3px;height:3px;border:1px solid #555;border-radius:50%;margin-right:5px;vertical-align:middle}

/* blog */
.post{position:absolute;top:1186px;width:116px;height:146px;background:#fff;box-shadow:0 3px 10px rgba(80,60,110,.12)}
.post-img{position:absolute;left:0;top:0;width:116px;height:86px}
.post-meta{position:absolute;left:11px;top:95px;font-size:3.7px;color:#555}
.post-title{position:absolute;left:11px;top:103px;width:96px;font-size:6.2px;font-weight:600;line-height:8px}
.post-more{position:absolute;left:11px;top:129px;width:20px;height:7px;background:var(--lilac);color:#fff;font-size:3.4px;display:flex;align-items:center;justify-content:center}

/* material cards */
.mat-card{position:absolute;width:96px;height:90px;background:#fff;box-shadow:0 3px 10px rgba(80,60,110,.13);text-align:center}
.mat-card svg{position:absolute;left:31px;top:16px}
.mat-card span{position:absolute;left:0;width:100%;top:66px;font-size:5.2px;font-weight:600}

/* category */
.side-row{position:absolute;left:32px;width:77px;font-size:4.3px;display:flex;justify-content:space-between;padding-bottom:3px;border-bottom:1px solid var(--line)}
.side-row b{font-weight:300;font-size:6px;line-height:4px}
.filter-title{position:absolute;left:32px;top:126px;font-size:7px;font-weight:500}
.size-chip{position:absolute;width:10px;height:9px;border:1px solid #ddd;font-size:3.3px;display:flex;align-items:center;justify-content:center;color:#555}
.radio{position:absolute;left:35px;font-size:3.8px;display:flex;align-items:center;gap:4px;color:#555}
.radio::before{content:"";width:4px;height:4px;border:1px solid #999;border-radius:50%}
.sort-box{position:absolute;left:314px;top:103px;width:81px;height:11px;border:1px solid var(--line);font-size:3.8px;display:flex;justify-content:space-between;align-items:center;padding:0 4px}
.prod{position:absolute;width:88px;height:105px;background:#fff;box-shadow:0 2px 9px rgba(80,60,110,.12)}
.prod-img{position:absolute;left:18px;top:12px;width:52px;height:52px;border-radius:3px}
.prod h5{position:absolute;left:9px;top:77px;font-size:4.6px;font-weight:600}
.prod p{position:absolute;left:9px;top:84px;width:72px;font-size:3.6px;line-height:5px;color:var(--grey)}
.pager{position:absolute;top:477px;height:10px;display:flex;align-items:center;font-size:3.8px}
.pill{height:9px;padding:0 6px;border-radius:5px;border:1px solid var(--line);display:flex;align-items:center}
.pill.on{background:var(--deep);color:#fff;border-color:var(--deep)}
.dot-on{width:9px;height:9px;border-radius:50%;background:var(--lilac);color:#fff;display:flex;align-items:center;justify-content:center}

/* product detail */
.detail-title{position:absolute;left:198px;top:124px;font-size:9px;font-weight:500}
.detail-text{position:absolute;left:198px;top:140px;width:175px;font-size:4px;line-height:6.6px;color:var(--grey)}
.rank-table{position:absolute;left:61px;top:203px;width:310px;border-collapse:collapse;font-size:5px}
.rank-table th{background:var(--lilac);color:#fff;font-size:3.8px;font-weight:500;height:9px;text-align:left;padding-left:34px}
.rank-table td{height:17px;padding-left:34px;position:relative}
.rank-table tr:nth-child(3) td{background:#f3eff7}
.rank-table td i{position:absolute;left:18px;top:4px;width:8px;height:8px;border-radius:50%}
.rank-table td i::after{content:"";position:absolute;left:2px;top:7px;width:4px;height:3px;background:#d9453c}

/* footer */
.foot{position:absolute;left:0;width:430px;height:153px;background:var(--footer);color:#fff}
.foot-logo{position:absolute;left:28px;top:58px;font-size:15px;font-weight:700}
.foot h4{font-size:5.4px;font-weight:600;margin-bottom:6px}
.foot-col{position:absolute;top:30px;font-size:3.9px;line-height:11px}
.foot-contact{left:212px}
.foot-contact li{position:relative;padding-left:8px;line-height:5.6px;margin-bottom:10px}
.foot-contact li::before{content:"";position:absolute;left:0;top:1px;width:3.5px;height:3.5px;border:0.8px solid #fff;border-radius:1px}
.foot-news{left:303px;line-height:5.5px}
.foot-news p{width:92px}
.foot-input{margin-top:6px;width:91px;height:13px;background:#fff;border-radius:7px;color:#777;display:flex;align-items:center;justify-content:space-between;padding-left:7px}
.foot-send{width:15px;height:13px;border-radius:7px;background:#c7b9da;display:flex;align-items:center;justify-content:center}
.socials{display:flex;gap:6px;margin-top:8px}
.socials span{width:9px;height:9px;border-radius:50%;border:0.8px solid rgba(255,255,255,.7)}
.foot-rule{position:absolute;left:28px;top:130px;width:372px;height:1px;background:rgba(255,255,255,.15)}
.foot-copy{position:absolute;left:0;width:430px;top:138px;text-align:center;font-size:3.8px;font-weight:600}
.foot-up{position:absolute;left:407px;top:113px;width:17px;height:17px;border-radius:50%;background:#fff;color:var(--deep);font-size:7px;display:flex;align-items:center;justify-content:center}
</style>
</head>
<body>

<!-- ============ HOME PAGE ============ -->
<section class="page" style="left:145px;top:176px;height:1541px">
  <header class="nav">
    <div class="nav-logo">Logo Here</div>
    <nav class="nav-menu"><span>HOME</span><span>COMPARE</span><span>CATEGORY</span><span>PRODUCT</span></nav>
    <div class="nav-user"><span class="avatar" role="img" aria-label="User profile photo"></span>Liam Porter ⌄</div>
  </header>
  <div class="hero hero-big">
    <div class="deco-blob" style="left:250px;top:40px;width:120px;height:120px"></div>
    <div class="deco-blob" style="left:20px;top:-30px;width:90px;height:90px"></div>
    <div class="deco-ring" style="left:354px;top:12px;width:6px;height:6px"></div>
    <div class="deco-diamond" style="left:374px;top:66px"></div>
    <div class="deco-plus" style="left:107px;top:82px">+</div>
    <h1 class="hero-title">What do you want to<br>glue together</h1>
  </div>
  <div class="picker" style="left:120px">
    <svg width="34" height="38" viewBox="0 0 34 38" fill="none" stroke="#fff" stroke-width="1.2"><rect x="7" y="11" width="20" height="25" rx="3"/><rect x="12" y="5" width="10" height="6"/><rect x="14" y="1" width="6" height="4"/><circle cx="17" cy="21" r="3"/><line x1="12" y1="28" x2="22" y2="28"/></svg>
    <div class="picker-label">Glue</div>
  </div>
  <div class="picker" style="left:223px">
    <svg width="34" height="38" viewBox="0 0 34 38" fill="none" stroke="#fff" stroke-width="1.2"><path d="M3 26 L13 17 L31 22 L21 32 Z"/><path d="M3 26 L3 30 L21 36 L21 32"/><path d="M21 36 L31 26 L31 22"/><path d="M9 19 L17 10 L29 14 L21 22"/></svg>
    <div class="picker-label">Metal</div>
  </div>
  <div class="vs">VS</div>

  <h2 class="section-title" style="top:247px">Find loan quickly</h2>
  <div class="finder-label" style="left:71px;top:289px"><span class="bottle-mini"></span>Glue metal to rubber</div>
  <div class="stepper" style="left:163px;top:287px;width:43px"><span>+</span><span>$1.000</span><span>-</span></div>
  <div class="track" style="left:72px;top:302px;width:135px"><span class="knob" style="left:78px"></span></div>
  <div class="finder-label" style="left:222px;top:289px"><span class="bottle-mini"></span>Metal and glue</div>
  <div class="stepper" style="left:318px;top:287px;width:43px"><span>+</span><span>$1.000</span><span>-</span></div>
  <div class="track" style="left:222px;top:302px;width:138px"><span class="knob" style="left:77px"></span></div>
  <div class="btn" style="left:181px;top:315px;width:67px;height:14px">↓ &nbsp;COMPARE OFFERS &nbsp;↑</div>
  <div class="rule" style="left:31px;top:358px;width:367px"></div>

  <h3 class="search-head">List of most popular searches</h3>
  <div class="round-arrow" style="left:65px;top:428px">←</div>
  <div class="round-arrow" style="left:95px;top:428px">→</div>
  <div class="tile" style="left:196px">
    <svg width="24" height="26" viewBox="0 0 24 26" fill="none" stroke="#fff" stroke-width="1"><rect x="2" y="10" width="9" height="14" rx="1"/><circle cx="16" cy="8" r="6"/><line x1="16" y1="2" x2="16" y2="14"/><line x1="10" y1="8" x2="22" y2="8"/></svg>
    <span>Metal to rubber</span>
  </div>
  <div class="tile" style="left:260px">
    <svg width="24" height="26" viewBox="0 0 24 26" fill="none" stroke="#fff" stroke-width="1"><rect x="9" y="2" width="6" height="6"/><line x1="2" y1="12" x2="22" y2="12"/><line x1="6" y1="12" x2="6" y2="24"/><line x1="18" y1="12" x2="18" y2="24"/><rect x="4" y="8" width="16" height="4"/></svg>
    <span>Glass to wood</span>
  </div>
  <div class="tile" style="left:324px">
    <svg width="24" height="26" viewBox="0 0 24 26" fill="none" stroke="#fff" stroke-width="1"><circle cx="12" cy="13" r="10"/><circle cx="12" cy="13" r="6"/><line x1="9" y1="9" x2="9" y2="17"/><line x1="12" y1="9" x2="12" y2="17"/><line x1="15" y1="9" x2="15" y2="17"/></svg>
    <span>Fabric to leather</span>
  </div>

  <div class="band" style="top:480px;height:214px"></div>
  <h2 class="section-title" style="top:508px">Popular products</h2>
  <div class="offer" style="top:528px"><div class="brand"><span class="brand-dot"></span><span class="brand-name">Adhera</span></div><span class="offer-divider"></span><ul class="perks"><li>Easy and intuitive website</li><li>Request a loan up to $35,000</li><li>Reasonable rates</li></ul><div class="rating"><span class="stars">★★★★☆</span>987 reviews</div><span class="apply">APPLY NOW</span><span class="users">567 people use it</span></div>
  <div class="offer" style="top:575px"><div class="brand"><span class="brand-dot"></span><span class="brand-name">Adhera</span></div><span class="offer-divider"></span><ul class="perks"><li>Easy and intuitive website</li><li>Request a loan up to $35,000</li><li>Reasonable rates</li></ul><div class="rating"><span class="stars">★★★★☆</span>987 reviews</div><span class="apply">APPLY NOW</span><span class="users">567 people use it</span></div>
  <div class="offer" style="top:622px"><div class="brand"><span class="brand-dot"></span><span class="brand-name">Adhera</span></div><span class="offer-divider"></span><ul class="perks"><li>Easy and intuitive website</li><li>Request a loan up to $35,000</li><li>Reasonable rates</li></ul><div class="rating"><span class="stars">★★★★☆</span>987 reviews</div><span class="apply">APPLY NOW</span><span class="users">567 people use it</span></div>

  <h2 class="faq-head">Frequently asked questions</h2>
  <div class="faq-item" style="top:755px"><b>+</b>Mauris morbi accumsan ipsum velit ?</div>
  <div class="faq-item" style="top:776px"><b>+</b>Aenean sollicitudin lorem quis bibendum auctor ?</div>
  <div class="faq-item" style="top:797px"><b>+</b>Elit consequat ipsum, nec sagittis sem nibh id elit ?</div>
  <div class="faq-item" style="top:817px"><b>+</b>Amet mauris. Morbi accumsan ipsum velit ?</div>
  <div class="faq-item" style="top:838px;border-bottom:none"><b>−</b>Sed non mauris vitae erat conseq ?</div>
  <p class="faq-answer">Aenean imperdiet etiam ultricies nisl vel augue curabitur ullamcor per ultricies nisi nam eget dui etiam rho tempus, tellus eget condi- mentum rhoncus, sem quam.</p>
  <div class="ph" role="img" aria-label="Large FAQ lettering with a thoughtful man beside a question mark" style="left:252px;top:722px;width:155px;height:182px;background:linear-gradient(160deg,#f4f3f6,#e6e4ea)"></div>

  <div class="ph" role="img" aria-label="Hot glue gun with craft tool blocks on a teal surface" style="left:65px;top:929px;width:147px;height:181px;background:linear-gradient(150deg,#a9bdb6,#8fa6a0)"></div>
  <div class="ph" role="img" aria-label="Smiling woman shrugging on a lilac background" style="left:0;top:1021px;width:100px;height:114px;background:linear-gradient(160deg,#c4b0de,#a98cc9);box-shadow:0 6px 14px rgba(60,40,90,.2)"></div>
  <div class="bio-kicker">Short</div>
  <h2 class="bio-title">Biography</h2>
  <span class="bio-line"></span>
  <p class="bio-text">Aenean imperdiet etiam ultricies nisl vel augue curabitur ullamcor per ultricies nisi nam eget dui etiam rho tempus, tellus eget ...</p>
  <ul class="bio-list">
    <li>Aenean sollicitudin, lorem quis bibendum</li>
    <li>Auctor, nisi elit consequat ipsum, nec sagittis id elit</li>
    <li>Duis sed odio sit amet nibh</li>
    <li>Culpulate cursus a sit amet mauris.</li>
    <li>Morbi accumsan ipsum velit. Nam nec tellus a odio</li>
    <li>Tincidunt auctor a ornare odio. Sed non mauris vitae</li>
    <li>Erat consequat auctor eu in elit class</li>
  </ul>

  <h2 class="section-title" style="top:1163px">Latest Blog</h2>
  <article class="post" style="left:32px"><div class="post-img" role="img" aria-label="Stacked wooden board samples" style="background:linear-gradient(135deg,#d7b48f,#a9825f)"></div><div class="post-meta">by Nora &nbsp;- &nbsp;January 2018</div><h3 class="post-title">01: Some blog heading goes right here..</h3><span class="post-more">MORE</span></article>
  <article class="post" style="left:157px"><div class="post-img" role="img" aria-label="Aluminium profile bars" style="background:linear-gradient(135deg,#c9c9cd,#77777d)"></div><div class="post-meta">by Nora &nbsp;- &nbsp;January 2018</div><h3 class="post-title">02: Some blog heading goes right here..</h3><span class="post-more">MORE</span></article>
  <article class="post" style="left:282px"><div class="post-img" role="img" aria-label="Row of rubber tyres" style="background:linear-gradient(135deg,#55555a,#222226)"></div><div class="post-meta">by Nora &nbsp;- &nbsp;January 2018</div><h3 class="post-title">03: Some blog heading goes right here..</h3><span class="post-more">MORE</span></article>

  <footer class="foot" style="top:1387px">
    <div class="foot-logo">Logo Here</div>
    <div class="foot-col" style="left:150px"><h4>Quick Links</h4><ul><li>Home</li><li>Compare</li><li>Category</li><li>Product</li></ul></div>
    <div class="foot-col foot-contact"><h4>Contact Info</h4><ul><li>Email:<br>info@example.com</li><li>Phone:<br>123-456-7890</li><li>Office Location:<br>Some address line goes here</li></ul></div>
    <div class="foot-col foot-news"><h4>Newsletter</h4><p>Subscribe to our email address to get the latest news.</p><div class="foot-input">Enter Your Email... <span class="foot-send">➤</span></div><div class="socials"><span></span><span></span><span></span></div></div>
    <div class="foot-up">↑</div>
    <div class="foot-rule"></div>
    <div class="foot-copy">COPYRIGHT 2020 ©. ALL RIGHT RESERVED</div>
  </footer>
</section>

<!-- ============ COMPARE PAGE ============ -->
<section class="page" style="left:625px;top:176px;height:1173px">
  <header class="nav">
    <div class="nav-logo">Logo Here</div>
    <nav class="nav-menu"><span>HOME</span><span>COMPARE</span><span>CATEGORY</span><span>PRODUCT</span></nav>
    <div class="nav-user"><span class="avatar" role="img" aria-label="User profile photo"></span>Liam Porter ⌄</div>
  </header>
  <div class="band" style="top:172px;height:531px"></div>
  <div class="hero hero-big">
    <div class="deco-blob" style="left:250px;top:40px;width:120px;height:120px"></div>
    <div class="deco-blob" style="left:20px;top:-30px;width:90px;height:90px"></div>
    <div class="deco-ring" style="left:354px;top:12px;width:6px;height:6px"></div>
    <div class="deco-diamond" style="left:374px;top:66px"></div>
    <div class="deco-plus" style="left:107px;top:82px">+</div>
    <h1 class="hero-title">What do you want to<br>glue together</h1>
  </div>
  <div class="picker" style="left:120px">
    <svg width="34" height="38" viewBox="0 0 34 38" fill="none" stroke="#fff" stroke-width="1.2"><rect x="7" y="11" width="20" height="25" rx="3"/><rect x="12" y="5" width="10" height="6"/><rect x="14" y="1" width="6" height="4"/><circle cx="17" cy="21" r="3"/><line x1="12" y1="28" x2="22" y2="28"/></svg>
    <div class="picker-label">Glue</div>
  </div>
  <div class="picker" style="left:223px">
    <svg width="34" height="38" viewBox="0 0 34 38" fill="none" stroke="#fff" stroke-width="1.2"><path d="M3 26 L13 17 L31 22 L21 32 Z"/><path d="M3 26 L3 30 L21 36 L21 32"/><path d="M21 36 L31 26 L31 22"/><path d="M9 19 L17 10 L29 14 L21 22"/></svg>
    <div class="picker-label">Metal</div>
  </div>
  <div class="vs">VS</div>

  <h2 class="section-title" style="top:235px">Popular products</h2>
  <div class="offer top-pick" style="top:257px"><div class="brand"><span class="brand-dot"></span><span class="brand-name">Adhera</span></div><span class="offer-divider"></span><ul class="perks"><li>Easy and intuitive website</li><li>Request a loan up to $35,000</li><li>Reasonable rates</li></ul><span class="medal"></span><div class="rating"><span class="stars">★★★★☆</span>987 reviews</div><span class="apply">APPLY NOW</span><span class="users">567 people use it</span></div>
  <div class="offer" style="top:304px"><div class="brand"><span class="brand-dot"></span><span class="brand-name">Adhera</span></div><span class="offer-divider"></span><ul class="perks"><li>Easy and intuitive website</li><li>Request a loan up to $35,000</li><li>Reasonable rates</li></ul><div class="rating"><span class="stars">★★★★☆</span>987 reviews</div><span class="apply">APPLY NOW</span><span class="users">567 people use it</span></div>
  <div class="offer" style="top:351px"><div class="brand"><span class="brand-dot"></span><span class="brand-name">Adhera</span></div><span class="offer-divider"></span><ul class="perks"><li>Easy and intuitive website</li><li>Request a loan up to $35,000</li><li>Reasonable rates</li></ul><div class="rating"><span class="stars">★★★★☆</span>987 reviews</div><span class="apply">APPLY NOW</span><span class="users">567 people use it</span></div>
  <div class="offer" style="top:397px"><div class="brand"><span class="brand-dot"></span><span class="brand-name">Adhera</span></div><span class="offer-divider"></span><ul class="perks"><li>Easy and intuitive website</li><li>Request a loan up to $35,000</li><li>Reasonable rates</li></ul><div class="rating"><span class="stars">★★★★☆</span>987 reviews</div><span class="apply">APPLY NOW</span><span class="users">567 people use it</span></div>
  <div class="offer" style="top:444px"><div class="brand"><span class="brand-dot"></span><span class="brand-name">Adhera</span></div><span class="offer-divider"></span><ul class="perks"><li>Easy and intuitive website</li><li>Request a loan up to $35,000</li><li>Reasonable rates</li></ul><div class="rating"><span class="stars">★★★★☆</span>987 reviews</div><span class="apply">APPLY NOW</span><span class="users">567 people use it</span></div>
  <div class="offer" style="top:491px"><div class="brand"><span class="brand-dot"></span><span class="brand-name">Adhera</span></div><span class="offer-divider"></span><ul class="perks"><li>Easy and intuitive website</li><li>Request a loan up to $35,000</li><li>Reasonable rates</li></ul><div class="rating"><span class="stars">★★★★☆</span>987 reviews</div><span class="apply">APPLY NOW</span><span class="users">567 people use it</span></div>
  <div class="offer" style="top:538px"><div class="brand"><span class="brand-dot"></span><span class="brand-name">Adhera</span></div><span class="offer-divider"></span><ul class="perks"><li>Easy and intuitive website</li><li>Request a loan up to $35,000</li><li>Reasonable rates</li></ul><div class="rating"><span class="stars">★★★★☆</span>987 reviews</div><span class="apply">APPLY NOW</span><span class="users">567 people use it</span></div>
  <div class="offer" style="top:584px"><div class="brand"><span class="brand-dot"></span><span class="brand-name">Adhera</span></div><span class="offer-divider"></span><ul class="perks"><li>Easy and intuitive website</li><li>Request a loan up to $35,000</li><li>Reasonable rates</li></ul><div class="rating"><span class="stars">★★★★☆</span>987 reviews</div><span class="apply">APPLY NOW</span><span class="users">567 people use it</span></div>
  <div class="offer" style="top:631px"><div class="brand"><span class="brand-dot"></span><span class="brand-name">Adhera</span></div><span class="offer-divider"></span><ul class="perks"><li>Easy and intuitive website</li><li>Request a loan up to $35,000</li><li>Reasonable rates</li></ul><div class="rating"><span class="stars">★★★★☆</span>987 reviews</div><span class="apply">APPLY NOW</span><span class="users">567 people use it</span></div>

  <h2 class="section-title" style="top:734px">Glue</h2>
  <div class="mat-card" style="left:65px;top:756px"><svg width="34" height="34" viewBox="0 0 34 34" fill="none" stroke="#876aae" stroke-width="1"><path d="M4 28 L20 12 L26 18 L10 34 Z"/><path d="M22 10 L28 4 L30 6 L24 12"/></svg><span>Glue Heading Here</span></div>
  <div class="mat-card" style="left:166px;top:756px"><svg width="34" height="34" viewBox="0 0 34 34" fill="none" stroke="#876aae" stroke-width="1"><rect x="6" y="2" width="10" height="14" rx="2"/><path d="M11 16 L22 28 Q26 32 30 30"/><line x1="8" y1="6" x2="14" y2="6"/></svg><span>Glue Heading Here</span></div>
  <div class="mat-card" style="left:268px;top:756px"><svg width="34" height="34" viewBox="0 0 34 34" fill="none" stroke="#876aae" stroke-width="1"><rect x="9" y="11" width="16" height="21" rx="2"/><rect x="13" y="5" width="8" height="6"/><line x1="17" y1="1" x2="17" y2="5"/><circle cx="17" cy="21" r="3"/></svg><span>Glue Heading Here</span></div>
  <div class="rule" style="left:32px;top:871px;width:366px"></div>
  <div class="mat-card" style="left:65px;top:896px"><svg width="34" height="34" viewBox="0 0 34 34" fill="none" stroke="#876aae" stroke-width="1"><path d="M3 30 L8 22 L16 22 L14 30 Z"/><path d="M16 30 L18 22 L26 22 L31 30 Z"/><path d="M10 22 L13 14 L21 14 L24 22"/><line x1="17" y1="2" x2="17" y2="8"/><line x1="8" y1="6" x2="11" y2="10"/><line x1="26" y1="6" x2="23" y2="10"/></svg><span>Metal Heading Here</span></div>
  <div class="mat-card" style="left:166px;top:896px"><svg width="34" height="34" viewBox="0 0 34 34" fill="none" stroke="#876aae" stroke-width="1"><ellipse cx="11" cy="8" rx="7" ry="4"/><path d="M4 8 V20 Q11 26 18 20 V8"/><circle cx="24" cy="22" r="8"/><line x1="18" y1="17" x2="30" y2="27"/></svg><span>Metal Heading Here</span></div>
  <div class="mat-card" style="left:268px;top:896px"><svg width="34" height="34" viewBox="0 0 34 34" fill="none" stroke="#876aae" stroke-width="1"><path d="M4 14 L12 4 L24 6 L31 16 L26 28 L12 30 L3 22 Z"/><path d="M12 4 L15 16 L31 16"/><path d="M15 16 L12 30"/></svg><span>Metal Heading Here</span></div>

  <footer class="foot" style="top:1020px">
    <div class="foot-logo">Logo Here</div>
    <div class="foot-col" style="left:150px"><h4>Quick Links</h4><ul><li>Home</li><li>Compare</li><li>Category</li><li>Product</li></ul></div>
    <div class="foot-col foot-contact"><h4>Contact Info</h4><ul><li>Email:<br>info@example.com</li><li>Phone:<br>123-456-7890</li><li>Office Location:<br>Some address line goes here</li></ul></div>
    <div class="foot-col foot-news"><h4>Newsletter</h4><p>Subscribe to our email address to get the latest news.</p><div class="foot-input">Enter Your Email... <span class="foot-send">➤</span></div><div class="socials"><span></span><span></span><span></span></div></div>
    <div class="foot-up">↑</div>
    <div class="foot-rule"></div>
    <div class="foot-copy">COPYRIGHT 2020 ©. ALL RIGHT RESERVED</div>
  </footer>
</section>

<!-- ============ CATEGORY PAGE ============ -->
<section class="page" style="left:625px;top:1383px;height:667px">
  <header class="nav">
    <div class="nav-logo">Logo Here</div>
    <nav class="nav-menu"><span>HOME</span><span>COMPARE</span><span>CATEGORY</span><span>PRODUCT</span></nav>
    <div class="nav-user"><span class="avatar" role="img" aria-label="User profile photo"></span>Liam Porter ⌄</div>
  </header>
  <div class="hero hero-slim">
    <div class="deco-ring" style="left:354px;top:10px;width:6px;height:6px"></div>
    <div class="deco-ring" style="left:354px;top:46px;width:6px;height:6px"></div>
    <h1 class="hero-title">Category</h1>
    <div class="crumbs">Home / Category</div>
  </div>
  <div class="side-row" style="top:105px"><span>Shop by Style</span><b>+</b></div>
  <div class="sort-box"><span><b>Sort:</b> Trending</span><span>+</span></div>
  <h3 class="filter-title">Filter</h3>
  <div class="side-row" style="top:141px"><span>Color</span><b>+</b></div>
  <div class="side-row" style="top:157px;border-bottom:none"><span>Size</span><b>−</b></div>
  <span class="size-chip" style="left:32px;top:173px">5</span><span class="size-chip" style="left:47px;top:173px">5.5</span><span class="size-chip" style="left:62px;top:173px">6</span><span class="size-chip" style="left:77px;top:173px">6.5</span><span class="size-chip" style="left:92px;top:173px">7</span>
  <span class="size-chip" style="left:32px;top:187px">7.5</span><span class="size-chip" style="left:47px;top:187px">8</span><span class="size-chip" style="left:62px;top:187px">8.5</span><span class="size-chip" style="left:77px;top:187px">9</span><span class="size-chip" style="left:92px;top:187px">9.5</span>
  <span class="size-chip" style="left:32px;top:201px">10</span><span class="size-chip" style="left:47px;top:201px">11</span><span class="size-chip" style="left:62px;top:201px">12</span><span class="size-chip" style="left:77px;top:201px">13</span>
  <div class="side-row" style="top:215px"><span>Price</span><b>−</b></div>
  <span class="radio" style="top:232px">Under $25</span>
  <span class="radio" style="top:244px">Under $50</span>
  <span class="radio" style="top:255px">Under $75</span>
  <span class="radio" style="top:267px">Under $100</span>
  <span class="radio" style="top:278px">Over $100</span>

  <div class="prod" style="left:126px;top:127px"><div class="prod-img" role="img" aria-label="Blue and yellow adhesive tin" style="background:linear-gradient(135deg,#4a8fd6,#e5c640)"></div><h5>Product Heading Here</h5><p>Lorem ipsum is simply dummy text of the printing and typesetting</p></div>
  <div class="prod" style="left:218px;top:127px"><div class="prod-img" role="img" aria-label="Cube of silver magnetic balls" style="background:radial-gradient(circle,#d8d8dc,#6d6d72)"></div><h5>Product Heading Here</h5><p>Lorem ipsum is simply dummy text of the printing and typesetting</p></div>
  <div class="prod" style="left:310px;top:127px"><div class="prod-img" role="img" aria-label="Dark metal plate" style="background:linear-gradient(135deg,#8a8a8e,#3a3a3e)"></div><h5>Product Heading Here</h5><p>Lorem ipsum is simply dummy text of the printing and typesetting</p></div>
  <div class="prod" style="left:126px;top:238px"><div class="prod-img" role="img" aria-label="Red and blue eraser block" style="background:linear-gradient(135deg,#e0643c,#3d7bc9)"></div><h5>Product Heading Here</h5><p>Lorem ipsum is simply dummy text of the printing and typesetting</p></div>
  <div class="prod" style="left:218px;top:238px"><div class="prod-img" role="img" aria-label="Small bottle of super glue" style="background:linear-gradient(180deg,#3f78c8,#f3f3f3)"></div><h5>Product Heading Here</h5><p>Lorem ipsum is simply dummy text of the printing and typesetting</p></div>
  <div class="prod" style="left:310px;top:238px"><div class="prod-img" role="img" aria-label="Assorted metal bearings and bolts" style="background:radial-gradient(circle,#c6c6ca,#77777c)"></div><h5>Product Heading Here</h5><p>Lorem ipsum is simply dummy text of the printing and typesetting</p></div>
  <div class="prod" style="left:126px;top:350px"><div class="prod-img" role="img" aria-label="Black hot glue gun" style="background:linear-gradient(135deg,#6a6a70,#1f1f23)"></div><h5>Product Heading Here</h5><p>Lorem ipsum is simply dummy text of the printing and typesetting</p></div>
  <div class="prod" style="left:218px;top:350px"><div class="prod-img" role="img" aria-label="Roll of black rubber sheet" style="background:linear-gradient(135deg,#555,#151515)"></div><h5>Product Heading Here</h5><p>Lorem ipsum is simply dummy text of the printing and typesetting</p></div>
  <div class="prod" style="left:310px;top:350px"><div class="prod-img" role="img" aria-label="Polished metal sphere" style="background:radial-gradient(circle at 40% 35%,#e2e4ea,#3e4250);border-radius:50%"></div><h5>Product Heading Here</h5><p>Lorem ipsum is simply dummy text of the printing and typesetting</p></div>

  <div class="pager" style="left:204px;gap:6px"><span class="pill">‹ Prev</span><span>1</span><span class="dot-on">2</span><span>3</span><span>...</span><span>82</span><span class="pill on">Next ›</span></div>

  <footer class="foot" style="top:514px">
    <div class="foot-logo">Logo Here</div>
    <div class="foot-col" style="left:150px"><h4>Quick Links</h4><ul><li>Home</li><li>Compare</li><li>Category</li><li>Product</li></ul></div>
    <div class="foot-col foot-contact"><h4>Contact Info</h4><ul><li>Email:<br>info@example.com</li><li>Phone:<br>123-456-7890</li><li>Office Location:<br>Some address line goes here</li></ul></div>
    <div class="foot-col foot-news"><h4>Newsletter</h4><p>Subscribe to our email address to get the latest news.</p><div class="foot-input">Enter Your Email... <span class="foot-send">➤</span></div><div class="socials"><span></span><span></span><span></span></div></div>
    <div class="foot-up">↑</div>
    <div class="foot-rule"></div>
    <div class="foot-copy">COPYRIGHT 2020 ©. ALL RIGHT RESERVED</div>
  </footer>
</section>

<!-- ============ PRODUCT PAGE ============ -->
<section class="page" style="left:145px;top:1747px;height:486px">
  <header class="nav">
    <div class="nav-logo">Logo Here</div>
    <nav class="nav-menu"><span>HOME</span><span>COMPARE</span><span>CATEGORY</span><span>PRODUCT</span></nav>
    <div class="nav-user"><span class="avatar" role="img" aria-label="User profile photo"></span>Liam Porter ⌄</div>
  </header>
  <div class="hero hero-slim">
    <div class="deco-ring" style="left:354px;top:10px;width:6px;height:6px"></div>
    <div class="deco-ring" style="left:354px;top:46px;width:6px;height:6px"></div>
    <h1 class="hero-title">Glue</h1>
    <div class="crumbs">Home / Category / Glue</div>
  </div>
  <div class="ph" role="img" aria-label="White glue bottle with red cap on a blue background" style="left:61px;top:109px;width:117px;height:67px;background:linear-gradient(135deg,#4f86c9,#2f5f9f)"></div>
  <h2 class="detail-title">Glue for metal</h2>
  <p class="detail-text">Lorem Ipsum is simply dummy text of the printing and typesetting industry. Lorem Ipsum has been the industry's standard dummy text ever since the 1500s, when an unknown printer took a galley of type and scrambled it to make a type specimen book. It has survived not only five centuries.</p>
  <table class="rank-table">
    <tr><th>BEST FOR</th><th>USED BY</th></tr>
    <tr><td><i style="background:#f2b531"></i>Gluing metal to rubber</td><td>Glass to fabric</td></tr>
    <tr><td><i style="background:#c5c6cc"></i>Glass to fabric</td><td>Glass to wood</td></tr>
    <tr><td><i style="background:#d98a45"></i>Glass to wood</td><td>Gluing metal to rubber</td></tr>
  </table>
  <h2 class="detail-title" style="left:61px;top:285px">Detail</h2>
  <p class="detail-text" style="left:61px;top:299px;width:312px">Lorem Ipsum is simply dummy text of the printing and typesetting industry. Lorem Ipsum has been the industry's standard dummy text ever since the 1500s, when an unknown printer took a galley of type and scrambled it to make a type specimen book.</p>

  <footer class="foot" style="top:335px">
    <div class="foot-logo">Logo Here</div>
    <div class="foot-col" style="left:150px"><h4>Quick Links</h4><ul><li>Home</li><li>Compare</li><li>Category</li><li>Product</li></ul></div>
    <div class="foot-col foot-contact"><h4>Contact Info</h4><ul><li>Email:<br>info@example.com</li><li>Phone:<br>123-456-7890</li><li>Office Location:<br>Some address line goes here</li></ul></div>
    <div class="foot-col foot-news"><h4>Newsletter</h4><p>Subscribe to our email address to get the latest news.</p><div class="foot-input">Enter Your Email... <span class="foot-send">➤</span></div><div class="socials"><span></span><span></span><span></span></div></div>
    <div class="foot-up">↑</div>
    <div class="foot-rule"></div>
    <div class="foot-copy">COPYRIGHT 2020 ©. ALL RIGHT RESERVED</div>
  </footer>
</section>

</body>
</html>
```